New Website design 2024: Ridgeline Flameguard, Inc.

1. Who we are: At Ridgeline Flameguard Inc, our mission is to provide our clients with comprehensive firestop and seismic expansion joint solutions that ensure the safety and integrity of their buildings. We specialize in the installation of firestop systems at penetrations, wall joints, and slab edge joints, as well as providing acoustical sealants, security sealants, architectural caulking, and seismic expansion joints. Since our establishment in 2007, we have been committed to improving the safety and integrity of buildings through our expertise and use of tested and approved firestop systems. Our focus is to deliver exceptional service and quality workmanship to ensure the protection of lives and property.
2. Services we provide:
-Firestopping: T-ratings, CMU Wall Joint, Exterior Caulking, Fireproof Patching, Head of Wall Joints, Through Penetrations, Curtain Wall/Slab Edge, Grease & Fume Duct Protection.
-Expansion Joints: Floor Covers, Roof Covers, Fire Barriers, Vapor Barriers, Wall & Ceiling Covers, Compression Seals, Pre-Compression Foams, Photoluminescent Signage
3. Examples of scope and projects we’ve completed.
4. How to contact us.: https://ridgelineflameguard.example/contact/
- Social Media Links: https://www.linkedin.example/company/ridgeline-flameguard/mycompany/
https://www.instagram.example/ridgelineflameguard/?hl=en
https://www.youtube.example/channel/UCQ8M2RT5KwpZdNvTeLoJbHs/videos
Target Market(s)
Commercial Construction industry
Industry/Entity Type
Commercial Construction industry in California
Coding
Coded - Design and coding required
Number of Pages Required
4 page
Colors
Designer to choose colors to be used in the design.
Requirements
Must have
- 1. Who we are. 2. Services we provide. 3. Examples of scope and projects we’ve completed. 4. How to contact us.
Nice to have
- Logo. Pictures of scope of work and pictures of projects completed or working on.
Should not have
- Names of clients.

```html
<!DOCTYPE html>
<html lang="en">
<head>
<meta charset="utf-8">
<title>Projects – Ridgeline Flameguard, Inc.</title>
<link rel="stylesheet" href="https://fonts.googleapis.com/css2?family=Unbounded:wght@700;800&family=Poppins:wght@400;500;600&family=Inter:wght@500;600&display=swap">
<style>
  :root {
    --ink: #111111;
    --footer: #171717;
    --white: #ffffff;
    --red: #e2231a;
    --blue: #1d5b9b;
    --text: #333333;
    --line: #5a5a5a;
  }
  * { box-sizing: border-box; margin: 0; padding: 0; }
  html, body { width: 1200px; height: 2440px; overflow: hidden; }
  body { position: relative; background: var(--white); font-family: "Poppins", sans-serif; color: var(--text); }

  .topbar { position: absolute; left: 0; top: 0; width: 1200px; height: 58px; background: var(--ink); color: var(--white); }
  .topbar__contact { position: absolute; left: 125px; top: 0; height: 58px; display: flex; align-items: center; gap: 18px; font-size: 13px; }
  .topbar__sep { opacity: .7; }
  .socials { display: flex; gap: 13px; }
  .topbar .socials { position: absolute; left: 968px; top: 15px; }
  .social { width: 27px; height: 27px; border: 1.5px solid var(--white); border-radius: 50%; display: block; }
  .footer .social { width: 32px; height: 32px; }

  .header { position: absolute; left: 0; top: 58px; width: 1200px; height: 80px; background: var(--white); }
  .brand { display: flex; align-items: center; gap: 8px; font-family: "Poppins", sans-serif; font-weight: 600; white-space: nowrap; }
  .brand__mark { width: 14px; height: 14px; }
  .header .brand { position: absolute; left: 125px; top: 27px; font-size: 18px; color: var(--red); }
  .header .brand__mark { background: var(--red); }
  .nav { position: absolute; left: 465px; top: 0; height: 80px; display: flex; align-items: center; gap: 25px; font-size: 12px; font-weight: 400; color: var(--ink); }
  .cta { position: absolute; left: 850px; top: 19px; width: 225px; height: 45px; }
  .cta__label { position: absolute; left: 0; top: 0; width: 180px; height: 45px; background: var(--blue); color: var(--white); font-family: "Inter", sans-serif; font-weight: 600; font-size: 13px; display: flex; align-items: center; justify-content: center; }
  .cta__icon { position: absolute; left: 0; top: 0; }

  .hero { position: absolute; left: 0; top: 138px; width: 1200px; height: 384px; background: linear-gradient(180deg, #3a3a3a 0%, #262626 45%, #0e0e0e 100%); text-align: center; color: var(--white); }
  .hero__eyebrow { position: absolute; left: 0; top: 143px; width: 1200px; font-family: "Inter", sans-serif; font-weight: 600; font-size: 20px; letter-spacing: 4px; }
  .hero__rule { position: absolute; top: 157px; height: 1px; background: rgba(255,255,255,.6); }
  .hero__title { position: absolute; left: 0; top: 180px; width: 1200px; font-family: "Unbounded", sans-serif; font-weight: 800; font-size: 37px; line-height: 47px; text-transform: uppercase; }

  .gallery { position: absolute; left: 0; top: 522px; width: 1200px; height: 1505px; text-align: center; }
  .gallery__eyebrow { position: absolute; left: 0; top: 94px; width: 1200px; font-family: "Inter", sans-serif; font-weight: 600; font-size: 20px; letter-spacing: 3.5px; color: var(--red); }
  .gallery__title { position: absolute; left: 0; top: 127px; width: 1200px; font-family: "Unbounded", sans-serif; font-weight: 800; font-size: 34px; color: var(--ink); text-transform: uppercase; }
  .gallery__intro { position: absolute; left: 250px; top: 195px; width: 700px; font-size: 12px; line-height: 22px; color: var(--text); }
  .tile { position: absolute; }
  .tile--worker { left: 125px; top: 290px; width: 463px; height: 473px; background: linear-gradient(160deg, #cfd3d4 0%, #a9aaa6 45%, #d7d2c9 100%); }
  .tile--deck { left: 612px; top: 290px; width: 463px; height: 225px; background: linear-gradient(180deg, #b9bbbc 0%, #c23a25 48%, #d0d0cc 70%, #bdbdbb 100%); }
  .tile--box { left: 612px; top: 538px; width: 463px; height: 225px; background: linear-gradient(135deg, #6f6f6c 0%, #b3442b 50%, #d8d2c4 100%); }
  .tile--pipes { left: 125px; top: 785px; width: 463px; height: 225px; background: linear-gradient(180deg, #8e949c 0%, #c7c6d0 55%, #e3e1e6 100%); }
  .tile--corner { left: 125px; top: 1033px; width: 463px; height: 225px; background: linear-gradient(180deg, #b9b6b2 0%, #a48a80 50%, #8d8c8a 100%); }
  .tile--joint { left: 612px; top: 785px; width: 463px; height: 473px; background: linear-gradient(135deg, #8c8a86 0%, #c8364b 40%, #9b9790 70%, #6d6a65 100%); }
  .loader { position: absolute; left: 575px; top: 1320px; width: 50px; height: 50px; }
  .loader__label { position: absolute; left: 0; top: 1384px; width: 1200px; font-size: 13px; color: var(--text); }

  .footer { position: absolute; left: 0; top: 2027px; width: 1200px; height: 413px; background: var(--footer); color: var(--white); text-align: center; }
  .footer .brand { position: absolute; left: 0; top: 80px; width: 1200px; justify-content: center; font-size: 19px; color: var(--white); }
  .footer .brand__mark { background: var(--white); }
  .footer__about { position: absolute; left: 250px; top: 155px; width: 700px; font-size: 12.5px; line-height: 22px; color: #e6e6e6; }
  .footer .socials { position: absolute; left: 535px; top: 229px; gap: 16px; }
  .footer__rule { position: absolute; left: 125px; top: 338px; width: 950px; height: 1px; background: var(--line); }
  .footer__copy { position: absolute; left: 0; top: 365px; width: 1200px; font-size: 12.5px; color: #e6e6e6; }
</style>
</head>
<body>
  <div class="topbar">
    <div class="topbar__contact"><span>555-010-0199</span><span class="topbar__sep">|</span><span>info@ridgelineflameguard.example</span></div>
    <div class="socials">
      <span class="social" role="img" aria-label="Social profile link"></span>
      <span class="social" role="img" aria-label="Photo profile link"></span>
      <span class="social" role="img" aria-label="Video channel link"></span>
    </div>
  </div>

  <header class="header">
    <div class="brand"><span class="brand__mark"></span>Ridgeline Flameguard</div>
    <nav class="nav"><span>Who We Are</span><span>Our Services</span><span>Our Projects</span></nav>
    <a class="cta" href="https://ridgelineflameguard.example/contact/">
      <svg class="cta__icon" width="225" height="45" viewBox="0 0 225 45" aria-hidden="true">
        <polygon points="168,0 225,0 225,45 182,45" fill="#e2231a"/>
        <circle cx="202" cy="22" r="7" fill="none" stroke="#fff" stroke-width="2.5"/>
        <circle cx="202" cy="22" r="2.5" fill="#fff"/>
      </svg>
      <span class="cta__label">Contact Us</span>
    </a>
  </header>

  <section class="hero" role="img" aria-label="Dark industrial photo of piping and flanged valves">
    <span class="hero__rule" style="left:315px;width:165px"></span>
    <span class="hero__rule" style="left:722px;width:163px"></span>
    <p class="hero__eyebrow">Projects</p>
    <h1 class="hero__title">Lorem Ipsum is a<br>dummy text</h1>
  </section>

  <section class="gallery">
    <p class="gallery__eyebrow">Gallery</p>
    <h2 class="gallery__title">Our Recent Projects</h2>
    <p class="gallery__intro">Lorem Ipsum is simply dummy text of the printing and typesetting industry. Lorem Ipsum has been the industry's standard dummy text ever since the 1500s,</p>

    <div class="tile tile--worker" role="img" aria-label="Installer in safety vest sealing an expansion joint beside a glass wall"></div>
    <div class="tile tile--deck" role="img" aria-label="Red firestop sealant along a fluted metal deck"></div>
    <div class="tile tile--box" role="img" aria-label="Electrical box wrapped in red firestop putty on a stud wall"></div>
    <div class="tile tile--pipes" role="img" aria-label="Pipe penetrations sealed with firestop collars on a slab"></div>
    <div class="tile tile--corner" role="img" aria-label="Insulated wall corner with red firestop tape"></div>
    <div class="tile tile--joint" role="img" aria-label="Cable bundles passing through a red fire barrier at a concrete slab"></div>

    <svg class="loader" viewBox="0 0 50 50" aria-hidden="true">
      <path d="M25 4 A21 21 0 1 1 6 34" fill="none" stroke="#1d5b9b" stroke-width="2"/>
      <path d="M25 12 A13 13 0 0 0 12 25" fill="none" stroke="#e2231a" stroke-width="2"/>
      <path d="M38 25 A13 13 0 0 1 30 37" fill="none" stroke="#e2231a" stroke-width="2"/>
    </svg>
    <p class="loader__label">Load More</p>
  </section>

  <footer class="footer">
    <div class="brand"><span class="brand__mark"></span>Ridgeline Flameguard</div>
    <p class="footer__about">Lorem Ipsum is simply dummy text of the printing and typesetting industry. Lorem Ipsum has been the industry's standard dummy text ever since the 1500s,</p>
    <div class="socials">
      <span class="social" role="img" aria-label="Social profile link"></span>
      <span class="social" role="img" aria-label="Photo profile link"></span>
      <span class="social" role="img" aria-label="Video channel link"></span>
    </div>
    <div class="footer__rule"></div>
    <p class="footer__copy">Copyright@2023-Ridgeline Flameguard-Privacy Policy</p>
  </footer>
</body>
</html>
```